Lumora Dwellings

Design a stylish Business card- we would like a businness card design that suits plastic business cards. Our card needs to show that we are tech savy and technology based so the design is crucial.

Target Market(s)

22-40

Industry/Entity Type

Plastic

Requirements
Must have
• attached is our logo. also double sided card would be nice.
my details

Tobias Fenwright
Director
0471596234
www.lumoradwellings.com.au
17 Ashcombe Lane, West Perth

```html
<!DOCTYPE html>
<html lang="en">
<head>
<meta charset="utf-8">
<title>Lumora Dwellings – Business Card</title>
<link href="https://fonts.googleapis.com/css2?family=Exo+2:ital,wght@0,400;0,600;1,400&display=swap" rel="stylesheet">
<style>
  :root{
    --page:#e4e5e7;
    --card:#1c1d1f;
    --silver:#c9ccd0;
    --muted:#9a9da2;
    --accent:#37b4e3;
    --line:#55585d;
    --panel-top:#2e3034;
    --panel-bottom:#222427;
  }
  *{box-sizing:border-box;margin:0;padding:0}
  html,body{width:1200px;height:900px;overflow:hidden}
  body{background:var(--page);font-family:"Exo 2",sans-serif;position:relative}
  .card{
    position:absolute;left:300px;width:600px;height:343px;
    background:var(--card);border-radius:6px;overflow:hidden;
    box-shadow:0 10px 28px rgba(0,0,0,.25);
  }
  .card--front{top:70px}
  .card--back{top:475px}
  .card__texture{
    position:absolute;inset:0;
    background:linear-gradient(135deg,#242528 0%,#1a1b1d 50%,#222326 100%);
  }
  .card__band{
    position:absolute;left:0;right:0;bottom:0;height:16px;
    background:var(--accent);border-top:3px solid var(--line);
  }
  .brand{position:absolute;left:0;right:0;top:130px;text-align:center}
  .brand__tagline{font-size:15px;color:var(--accent);letter-spacing:.5px;margin-bottom:10px}
  .brand__name{
    font-size:48px;font-weight:600;color:var(--silver);letter-spacing:2px;
    display:inline-flex;align-items:center;gap:16px;
  }
  .brand__mark{width:22px;height:22px;background:var(--accent);border-radius:50%}
  .person{position:absolute;left:52px;top:86px;color:var(--silver)}
  .person__name{font-size:24px;font-weight:600;letter-spacing:.5px}
  .person__role{font-size:17px;font-style:italic;color:var(--muted);margin-top:2px}
  .contact{list-style:none;margin-top:28px;font-size:18px;color:var(--muted);line-height:1.45}
  .contact__key{color:var(--muted);margin-right:8px}
  .contact__indent{padding-left:32px}
  .device-panel{
    position:absolute;right:32px;top:0;width:242px;height:86px;
    border-radius:0 0 16px 16px;
    background:linear-gradient(180deg,var(--panel-top),var(--panel-bottom));
  }
  .device-key{
    position:absolute;right:36px;top:100px;width:74px;height:74px;border-radius:14px;
    background:linear-gradient(180deg,var(--panel-top),var(--panel-bottom));
  }
</style>
</head>
<body>
  <section class="card card--front" aria-label="Card front">
    <div class="card__texture" role="img" aria-label="Dark repeating arrow pattern texture"></div>
    <div class="brand">
      <p class="brand__tagline">Smarter Living At Your Fingertips</p>
      <h1 class="brand__name"><span class="brand__mark"></span>Lumora Dwellings</h1>
    </div>
    <div class="card__band"></div>
  </section>

  <section class="card card--back" aria-label="Card back">
    <div class="card__texture" role="img" aria-label="Dark repeating arrow pattern texture"></div>
    <div class="person">
      <h2 class="person__name">Tobias Fenwright</h2>
      <p class="person__role">Director</p>
      <ul class="contact">
        <li><span class="contact__key">[t]</span>0471 596 234</li>
        <li><span class="contact__key">[w]</span>www.lumoradwellings.com.au</li>
        <li><span class="contact__key">[a]</span>17 Ashcombe Lane</li>
        <li class="contact__indent">West Perth</li>
      </ul>
    </div>
    <div class="device-panel" role="img" aria-label="Illustrated panel of smart home device icons"></div>
    <div class="device-key" role="img" aria-label="Illustrated power button"></div>
    <div class="card__band"></div>
  </section>
</body>
</html>
```